Harbor Nightclub

Nightclub flyer., digital single sided, for KV and PX. I included samples of some previous flyers we've used. Sample Info:
HARBOR
FRIDAYS
FRI MAY 1 2020
DJ VORTAN (club floor)
DJ RUZO & DJ TAV (residents on the lounge floor)
4217 Marlow Avenue Sacramento
www.harborvenuehall.example for list/VIP inquiries

Target Market(s)

Upscale top 40 crowd but want some cool and artsy like the examples included.

Font styles to use
Sans Serif

Requirements
Must have
• Harbor Logo
Nice to have
• Would be nice if the flyer can be incorporated later with DJ photos (sometimes we will add dj photos to pixagram etc). Would like a big city type of feel.
Should not have
• Nothing too sexual.

```html
<!DOCTYPE html>
<html lang="en">
<head>
<meta charset="utf-8">
<title>Harbor Fridays</title>
<link rel="stylesheet" href="https://fonts.googleapis.com/css2?family=Montserrat:wght@400;600&family=Open+Sans:wght@400;600&family=Oswald:wght@500&display=swap">
<style>
  :root {
    --sky-top: #9c7cc0;
    --sky-mid: #c56a9c;
    --glow: #f3a2a0;
    --dusk: #6a3f8c;
    --deep: #2f2f78;
    --ink: #ffffff;
    --ink-soft: rgba(255,255,255,0.85);
    --mark: #c9c66a;
    --mark-text: #3b3440;
    --date-bg: #3a2e3a;
  }
  html, body {
    margin: 0;
    padding: 0;
    overflow: hidden;
    background: #1d1a2e;
  }
  .flyer {
    position: relative;
    width: 816px;
    height: 1200px;
    overflow: hidden;
    font-family: "Open Sans", Arial, sans-serif;
    color: var(--ink);
  }
  .city-backdrop {
    position: absolute;
    inset: 0;
    background:
      radial-gradient(ellipse 300px 220px at 400px 470px, rgba(255,170,160,0.85), rgba(255,170,160,0) 70%),
      radial-gradient(ellipse 520px 380px at 420px 500px, rgba(214,90,140,0.55), rgba(214,90,140,0) 75%),
      linear-gradient(180deg, var(--sky-top) 0%, #b68ac4 18%, var(--sky-mid) 40%, var(--dusk) 62%, #4a3a88 80%, var(--deep) 100%);
  }
  .geometry {
    position: absolute;
    inset: 0;
  }
  .brand {
    position: absolute;
    left: 0;
    width: 816px;
    top: 20px;
    text-align: center;
  }
  .brand-dot {
    display: block;
    width: 104px;
    height: 104px;
    margin: 0 auto;
    border-radius: 50%;
    background: var(--mark);
  }
  .brand-name {
    display: block;
    margin-top: 40px;
    font-family: "Montserrat", Arial, sans-serif;
    font-weight: 400;
    font-size: 50px;
    letter-spacing: 3px;
    line-height: 1;
    color: var(--mark-text);
  }
  .date-badge {
    position: absolute;
    left: 597px;
    top: 247px;
    width: 128px;
    height: 128px;
  }
  .date-text {
    position: absolute;
    left: 597px;
    top: 264px;
    width: 128px;
    text-align: center;
    font-family: "Open Sans", Arial, sans-serif;
    line-height: 1;
  }
  .date-day, .date-month { font-size: 16px; display: block; }
  .date-num { font-size: 36px; display: block; margin: 3px 0 4px; }
  .intro {
    position: absolute;
    left: 0;
    width: 816px;
    top: 350px;
    text-align: center;
    font-family: "Oswald", Arial, sans-serif;
    font-weight: 500;
    font-size: 17px;
    letter-spacing: 1.5px;
  }
  .intro-rule {
    position: absolute;
    left: 373px;
    top: 338px;
    width: 86px;
    height: 2px;
    background: var(--ink-soft);
  }
  .event-title {
    position: absolute;
    left: 0;
    width: 816px;
    top: 400px;
    margin: 0;
    text-align: center;
    font-weight: 400;
    line-height: 1;
  }
  .event-title .line-main {
    display: block;
    font-size: 112px;
    letter-spacing: 2px;
  }
  .event-title .line-sub {
    display: block;
    margin-top: 0;
    font-size: 74px;
    letter-spacing: 2px;
  }
  .lineup {
    position: absolute;
    left: 0;
    width: 816px;
    top: 784px;
    text-align: center;
  }
  .lineup-label {
    font-family: "Montserrat", Arial, sans-serif;
    font-weight: 600;
    font-size: 14px;
    letter-spacing: 5px;
    margin: 0 0 17px;
  }
  .lineup-act {
    margin: 0 0 22px;
    font-size: 21px;
    line-height: 1.2;
  }
  .info-rule {
    position: absolute;
    left: 188px;
    top: 937px;
    width: 443px;
    height: 3px;
    border-radius: 2px;
    background: rgba(255,255,255,0.7);
  }
  .web {
    position: absolute;
    left: 0;
    width: 816px;
    top: 962px;
    text-align: center;
    font-family: "Montserrat", Arial, sans-serif;
    font-size: 16px;
    letter-spacing: 3.4px;
  }
  .info-label {
    position: absolute;
    left: 0;
    width: 816px;
    top: 1007px;
    text-align: center;
    font-family: "Montserrat", Arial, sans-serif;
    font-size: 11px;
  }
  .ticket {
    position: absolute;
    top: 1041px;
    height: 24px;
    border: 2px solid rgba(255,255,255,0.75);
    border-radius: 4px;
    text-align: center;
    font-size: 18px;
    line-height: 24px;
    letter-spacing: 1px;
  }
  .ticket-entry { left: 262px; width: 136px; }
  .ticket-vip { left: 416px; width: 135px; }
  .address {
    position: absolute;
    left: 0;
    width: 816px;
    top: 1118px;
    text-align: center;
    font-size: 22px;
    letter-spacing: 0.5px;
  }
</style>
</head>
<body>
<main class="flyer">
  <div class="city-backdrop" role="img" aria-label="Dusk cityscape with a clock tower, bridge and river under a violet and pink sky"></div>

  <svg class="geometry" width="816" height="1200" viewBox="0 0 816 1200" aria-hidden="true">
    <g fill="none" stroke="rgba(255,255,255,0.35)" stroke-width="1">
      <polygon points="408,150 700,700 116,700"/>
      <polygon points="408,800 80,240 736,240"/>
      <polygon points="408,260 620,470 408,680 196,470"/>
      <polygon points="408,300 580,470 408,640 236,470" stroke="rgba(255,255,255,0.22)"/>
      <line x1="0" y1="60" x2="816" y2="30"/>
      <line x1="0" y1="190" x2="816" y2="250"/>
      <polygon points="408,800 300,1000 516,1000" stroke="rgba(255,255,255,0.25)"/>
      <polyline points="20,770 408,700 796,770"/>
    </g>
    <polygon points="408,290 590,470 408,650 226,470" fill="rgba(255,220,220,0.16)"/>
    <polygon points="408,330 550,470 408,610 266,470" fill="rgba(255,200,200,0.12)"/>
  </svg>

  <header class="brand">
    <span class="brand-dot"></span>
    <span class="brand-name">HARBOR</span>
  </header>

  <svg class="date-badge" viewBox="0 0 128 128" aria-hidden="true">
    <polygon points="64,0 128,64 64,128 0,64" fill="var(--date-bg)"/>
  </svg>
  <div class="date-text">
    <span class="date-day">FRI</span>
    <span class="date-num">01</span>
    <span class="date-month">MAY</span>
  </div>

  <div class="intro-rule"></div>
  <p class="intro">WE PRESENT TO YOU:</p>

  <h1 class="event-title">
    <span class="line-main">HARBOR</span>
    <span class="line-sub">FRIDAYS</span>
  </h1>

  <section class="lineup">
    <p class="lineup-label">LIVE PERFORMANCE:</p>
    <p class="lineup-act">DJ VORTAN (CLUB FLOOR)</p>
    <p class="lineup-act">DJ RUZO &amp; DJ TAV (RESIDENTS ON THE LOUNGE FLOOR)</p>
  </section>

  <div class="info-rule"></div>
  <p class="web" style="margin:0">www.harborvenuehall.example for list/VIP inquiries</p>
  <p class="info-label" style="margin:0">EVENT INFORMATION:</p>
  <div class="ticket ticket-entry">ENTRY: $</div>
  <div class="ticket ticket-vip">VIP</div>
  <p class="address" style="margin:0">4217 MARLOW AVENUE SACRAMENTO</p>
</main>
</body>
</html>
```